Redesign of Business Card to look more professional and stand out

Business card design. You can lean more about our company by going to dlmfabworks.example. Raised letters would be nice. Company name & Address
DL&M
418 Wrenfield Crest Drive, Suite 140
Birmingham, AL 35999

You can use my name and title: Glenn Marlowe
Business Development Manager

Target Market(s)

Heavy Industrial market, i.e. utilities, chemical plants, paper mills, construction companies

Industry/Entity Type

Construction

Contact Information for Business Card

We provide Project Management & Project Support Services

Font styles to use
Serif

Requirements
Must have
• Company name & Address
• DL&M
• 418 Wrenfield Crest Drive, Suite 140
• Birmingham, AL 35999
Nice to have
• ideas for the back of the card
Should not have
• no crazy colors. needs to look professional and standout.

```html
<!DOCTYPE html>
<html lang="en">
<head>
<meta charset="utf-8">
<title>DL&amp;M Business Card</title>
<link href="https://fonts.googleapis.com/css2?family=Open+Sans:ital,wght@0,400;0,700;1,400&display=swap" rel="stylesheet">
<style>
  :root {
    --backdrop: #e9e7e4;
    --card: #1c1c1d;
    --card-edge: #2a2a2b;
    --name-blue: #3a5fae;
    --text-light: #eeeeee;
    --text-muted: #8d8d90;
    --divider: #6a6a6d;
  }
  * { box-sizing: border-box; margin: 0; padding: 0; }
  html, body { width: 1200px; height: 814px; overflow: hidden; }
  body {
    background: var(--backdrop);
    font-family: "Open Sans", Arial, sans-serif;
    display: flex;
    align-items: center;
    justify-content: center;
    gap: 40px;
  }
  .card {
    width: 520px;
    height: 297px;
    background: var(--card);
    border: 1px solid var(--card-edge);
    border-radius: 4px;
    position: relative;
    box-shadow: 0 6px 18px rgba(0,0,0,0.25);
  }
  .company-name {
    position: absolute;
    font-weight: 700;
    font-size: 40px;
    color: var(--text-light);
    line-height: 1;
    white-space: nowrap;
  }
  .card-back .company-name { left: 190px; top: 110px; }
  .card-back .tagline {
    position: absolute;
    left: 40px;
    top: 190px;
    font-style: italic;
    font-size: 13px;
    color: var(--text-light);
    white-space: nowrap;
  }
  .card-front .company-name { left: 240px; top: 62px; }
  .identity {
    position: absolute;
    right: 270px;
    top: 150px;
    text-align: right;
    line-height: 1.35;
    white-space: nowrap;
  }
  .identity .person-name { color: var(--name-blue); font-weight: 700; font-size: 17px; }
  .identity .person-title { color: var(--text-muted); font-size: 12.5px; }
  .identity .address { color: var(--text-light); font-size: 12.5px; }
  .divider {
    position: absolute;
    left: 262px;
    top: 176px;
    width: 1px;
    height: 84px;
    background: var(--divider);
  }
  .contacts {
    position: absolute;
    left: 276px;
    top: 176px;
    list-style: none;
  }
  .contacts li {
    display: flex;
    align-items: center;
    gap: 8px;
    color: var(--text-light);
    font-size: 13px;
    height: 21px;
    white-space: nowrap;
  }
  .contacts svg { width: 12px; height: 12px; fill: var(--name-blue); flex: none; }
</style>
</head>
<body>
  <section class="card card-back" aria-label="Card back">
    <div class="company-name">DL&amp;M</div>
    <p class="tagline">We provide Project Management &amp; Project Support Services</p>
  </section>

  <section class="card card-front" aria-label="Card front">
    <div class="company-name">DL&amp;M</div>
    <div class="identity">
      <div class="person-name">Glenn Marlowe</div>
      <div class="person-title">Business Development Manager</div>
      <div class="address">418 Wrenfield Crest Drive, Suite 140</div>
      <div class="address">Birmingham, AL 35999</div>
    </div>
    <div class="divider"></div>
    <ul class="contacts">
      <li>
        <svg viewBox="0 0 24 24"><path d="M6.6 10.8a15.1 15.1 0 0 0 6.6 6.6l2.2-2.2c.3-.3.7-.4 1-.2 1.1.4 2.3.6 3.6.6.6 0 1 .4 1 1V20c0 .6-.4 1-1 1A17 17 0 0 1 3 4c0-.6.4-1 1-1h3.5c.6 0 1 .4 1 1 0 1.3.2 2.5.6 3.6.1.3 0 .7-.2 1z"/></svg>
        205-555-0142
      </li>
      <li>
        <svg viewBox="0 0 24 24"><path d="M7 1h10a2 2 0 0 1 2 2v18a2 2 0 0 1-2 2H7a2 2 0 0 1-2-2V3a2 2 0 0 1 2-2zm0 3v15h10V4z"/></svg>
        205-555-0143
      </li>
      <li>
        <svg viewBox="0 0 24 24"><path d="M2 5h20v14H2zm2 2v.5l8 5 8-5V7z"/></svg>
        glenn@dlmfabworks.example
      </li>
      <li>
        <svg viewBox="0 0 24 24"><circle cx="12" cy="12" r="10"/></svg>
        www.dlmfabworks.example
      </li>
    </ul>
  </section>
</body>
</html>
```